Bluefield construction business cards

I need a business card with a replacement window photo or graphic on it .phone # 919 482 -7731 bluefieldconstruction@mailbox-example.com fax #919 274-8093 '' The Window Replacement Specialist"

Industry/Entity Type

Construction

```html
<!DOCTYPE html>
<html lang="en">
<head>
<meta charset="utf-8">
<title>Bluefield Construction – Business Cards</title>
<link rel="stylesheet" href="https://fonts.googleapis.com/css2?family=Oswald:wght@600&family=Arimo:wght@400&display=swap">
<style>
  :root {
    --page-bg: #f1f1f1;
    --lime: #55ff00;
    --white: #ffffff;
    --frame-dark: #2f9e12;
    --brand-green: #4ee01a;
    --pane: #eef1ee;
    --text-light: #ffffff;
  }
  * { margin: 0; padding: 0; box-sizing: border-box; }
  html, body {
    width: 1200px; height: 1001px; overflow: hidden;
    background: var(--page-bg);
  }
  .canvas { position: relative; width: 1200px; height: 1001px; }

  .card {
    position: absolute;
    width: 520px; height: 300px;
    box-shadow: 0 6px 18px rgba(0,0,0,0.12);
  }
  .card--front { left: 90px; top: 170px; background: var(--lime); color: var(--text-light); }
  .card--back  { left: 590px; top: 530px; background: var(--white); color: var(--brand-green); }

  .brand {
    position: absolute; left: 46px; top: 62px;
    font-family: "Oswald", sans-serif; font-weight: 600;
    color: inherit; line-height: 1;
  }
  .brand__name { display: block; font-size: 46px; letter-spacing: 0.5px; }
  .brand__sub  { display: block; font-size: 17px; letter-spacing: 4px; margin: 4px 0 0 30px; }

  .tagline {
    position: absolute; left: 46px; top: 150px; width: 262px;
    font-family: "Arimo", sans-serif; font-size: 12px; letter-spacing: 0.3px;
    text-transform: uppercase; text-align: center; white-space: nowrap;
    padding: 3px 0;
    border-top: 2px solid currentColor; border-bottom: 2px solid currentColor;
  }

  .contacts {
    position: absolute; left: 46px; top: 198px; list-style: none;
    font-family: "Arimo", sans-serif; font-size: 13px;
  }
  .contacts__item { display: flex; align-items: center; gap: 10px; height: 24px; }
  .contacts__icon { width: 15px; height: 15px; flex: none; }

  .window { position: absolute; right: 36px; top: 34px; width: 150px; height: 232px; }
</style>
</head>
<body>
<main class="canvas">

  <section class="card card--front" aria-label="Business card front">
    <div class="brand">
      <span class="brand__name">Bluefield</span>
      <span class="brand__sub">Construction</span>
    </div>
    <p class="tagline">The Window Replacement Specialist</p>
    <ul class="contacts">
      <li class="contacts__item">
        <svg class="contacts__icon" viewBox="0 0 16 16" aria-hidden="true"><path d="M4 1.5h2.2l1 3.3-1.5 1.2a8 8 0 0 0 4.3 4.3l1.2-1.5 3.3 1v2.2c0 .9-.8 1.5-1.6 1.4C6.9 13 3 9.1 2.6 3.1 2.5 2.3 3.1 1.5 4 1.5z" fill="currentColor"/></svg>
        #919 482 -7731
      </li>
      <li class="contacts__item">
        <svg class="contacts__icon" viewBox="0 0 16 16" aria-hidden="true"><rect x="4" y="1.5" width="8" height="5" fill="none" stroke="currentColor" stroke-width="1.4"/><rect x="1" y="6" width="14" height="7" rx="1" fill="currentColor"/><rect x="4" y="10" width="8" height="4.5" fill="var(--lime)" stroke="currentColor" stroke-width="1.2"/></svg>
        #919 274-8093
      </li>
      <li class="contacts__item">
        <svg class="contacts__icon" viewBox="0 0 16 16" aria-hidden="true"><rect x="1" y="3" width="14" height="10" fill="currentColor"/><path d="M1.5 3.5 8 9l6.5-5.5" fill="none" stroke="var(--lime)" stroke-width="1.4"/></svg>
        bluefieldconstruction@mailbox-example.com
      </li>
    </ul>
    <svg class="window" viewBox="0 0 150 232" role="img" aria-label="Six-pane replacement window graphic">
      <rect x="4" y="4" width="142" height="224" fill="none" stroke="var(--frame-dark)" stroke-width="8"/>
      <rect x="16" y="16" width="118" height="200" fill="var(--white)"/>
      <g fill="var(--pane)">
        <rect x="25" y="25" width="46" height="55"/><rect x="79" y="25" width="46" height="55"/>
        <rect x="25" y="88" width="46" height="56"/><rect x="79" y="88" width="46" height="56"/>
        <rect x="25" y="152" width="46" height="55"/><rect x="79" y="152" width="46" height="55"/>
      </g>
    </svg>
  </section>

  <section class="card card--back" aria-label="Business card back">
    <div class="brand">
      <span class="brand__name">Bluefield</span>
      <span class="brand__sub">Construction</span>
    </div>
    <p class="tagline">The Window Replacement Specialist</p>
    <svg class="window" viewBox="0 0 150 232" role="img" aria-label="Six-pane replacement window graphic">
      <rect x="4" y="4" width="142" height="224" fill="none" stroke="var(--frame-dark)" stroke-width="8"/>
      <rect x="16" y="16" width="118" height="200" fill="var(--white)"/>
      <g fill="var(--pane)">
        <rect x="25" y="25" width="46" height="55"/><rect x="79" y="25" width="46" height="55"/>
        <rect x="25" y="88" width="46" height="56"/><rect x="79" y="88" width="46" height="56"/>
        <rect x="25" y="152" width="46" height="55"/><rect x="79" y="152" width="46" height="55"/>
      </g>
    </svg>
  </section>

</main>
</body>
</html>
```